TQR Flyer

We need a two sided flyer that matches the color scheme of the logo. Should use left justified formatting. Needs to reflect diversity in terms of race and gender. Should have a clean and uncluttered look and feel. Add the following tag line: Guiding Public Sector Teams Toward Smarter Work

```html
<!DOCTYPE html>
<html lang="en">
<head>
<meta charset="utf-8">
<title>TQR Flyer</title>
<link rel="stylesheet" href="https://fonts.googleapis.com/css2?family=Arimo:wght@400;700&family=Catamaran:wght@700;800&display=swap">
<style>
  :root {
    --band: #c9b664;
    --olive: #776915;
    --olive-dark: #6b5e12;
    --mark-light: #ddd09a;
    --gold: #f2c479;
    --gold-soft: #e9c985;
    --tagline: #e3b870;
    --white: #ffffff;
  }
  * { margin: 0; padding: 0; box-sizing: border-box; }
  html, body { width: 840px; height: 1200px; overflow: hidden; }
  body { background: var(--olive); font-family: "Arimo", Arial, sans-serif; color: var(--white); }
  .flyer { position: relative; width: 840px; height: 1200px; background: var(--olive); }
  .top-band { position: absolute; left: 0; top: 0; width: 840px; height: 152px; background: var(--band); }
  .brand-dot { position: absolute; left: 352px; top: 16px; width: 122px; height: 122px; border-radius: 50%; background: var(--olive-dark); }
  .brand-name { position: absolute; left: 490px; top: 18px; font-family: "Arimo", Arial, sans-serif; font-weight: 700; font-size: 104px; line-height: 1; color: var(--mark-light); letter-spacing: 2px; }
  .title { position: absolute; left: 122px; top: 162px; font-family: "Catamaran", sans-serif; font-weight: 800; font-size: 44px; line-height: 1.2; }
  .tagline { position: absolute; left: 206px; top: 217px; font-size: 16px; color: var(--tagline); }
  .intro { position: absolute; left: 100px; width: 640px; top: 256px; text-align: center; font-size: 17.5px; line-height: 1.3; }
  .focus-list { position: absolute; left: 68px; top: 326px; width: 720px; list-style: none; }
  .focus-list li { position: relative; padding-left: 58px; font-size: 21.5px; line-height: 1.25; margin-bottom: 12px; }
  .bullet { position: absolute; width: 22px; height: 22px; border-radius: 50%; background: var(--gold); }
  .focus-list .bullet { left: 2px; top: 2px; }
  .experience { position: absolute; left: 122px; top: 468px; width: 643px; font-size: 19px; line-height: 1.35; text-align: justify; }
  .services-heading { position: absolute; left: 122px; top: 592px; font-size: 31px; font-weight: 700; color: var(--gold); }
  .services-sub { position: absolute; left: 122px; top: 630px; font-size: 17px; font-weight: 700; color: var(--gold); }
  .services-sub .aka { font-size: 21px; }
  .services-text { position: absolute; left: 118px; top: 664px; width: 646px; font-size: 18.5px; line-height: 1.36; color: var(--gold-soft); text-align: justify; }
  .services-text strong { color: var(--white); }
  .deliverables-heading { position: absolute; left: 120px; top: 848px; font-size: 18.5px; font-weight: 400; }
  .deliverables { position: absolute; left: 86px; top: 880px; width: 720px; list-style: none; }
  .deliverables li { position: relative; padding-left: 36px; font-size: 15.5px; height: 30.5px; line-height: 20px; }
  .deliverables .bullet { left: 0; top: 0; width: 18px; height: 18px; }
  .reg { font-size: 10px; vertical-align: super; }
</style>
</head>
<body>
<main class="flyer">
  <header class="top-band">
    <span class="brand-dot"></span>
    <span class="brand-name">TQR</span>
  </header>

  <h1 class="title">Torvale Quest Resources</h1>
  <p class="tagline">Guiding Public Sector Teams Toward Smarter Work</p>

  <p class="intro">TQR is a public sector focused management consulting firm providing facilitation and advisory support services in the areas of:</p>

  <ul class="focus-list">
    <li><span class="bullet"></span>Strategic planning, utilizing the proprietary Single Sheet Strategy Plan<span class="reg">®</span> Model (also known as the S3P®)</li>
    <li><span class="bullet"></span>Performance Management and Data Analytics (tracking and measuring what matters, while also driving desired results)</li>
  </ul>

  <p class="experience">TQR is able to bring to any engagement experienced consultants with decades of knowledge and experience garnered from working at all levels of government as chief financial officer, chief procurement officer, chief operating officer and as city manager.</p>

  <h2 class="services-heading">Our Services</h2>
  <p class="services-sub">The Single Sheet Strategy Plan® <span class="aka">(aka S3P®)</span></p>
  <p class="services-text"><strong>"A Family of Single Sheet Tools®"</strong> custom fit to the organization and the business situation at hand. The work group is the top management team for the organization, who are responsible for overall strategic direction of the organization. "The process involves an initial strategic assessment, 2-3 work sessions with strategic mapping homework in between each session, over an 8-10 week time span.".</p>

  <h3 class="deliverables-heading">S3P® Deliverables</h3>
  <ul class="deliverables">
    <li><span class="bullet"></span>An actionable strategic plan on one page - S3P®: Objective, Goals, Strategies, Plans.</li>
    <li><span class="bullet"></span>Critical path detail for each S3P® page Plan.</li>
    <li><span class="bullet"></span>S3P Progress Card® to teach progress of all desired outcomes.</li>
    <li><span class="bullet"></span>Hold Back Register® to clearly outline work to Stop, Hold or Limit.</li>
    <li><span class="bullet"></span>Resources &amp; Barriers analysis to align capability with commitments.</li>
    <li><span class="bullet"></span>Assessment of "relative priority" across all key projects.</li>
    <li><span class="bullet"></span>Deployment plan – initial and on-going.</li>
    <li><span class="bullet"></span>Periodic Review and annual renewal of the strategic plan.</li>
    <li><span class="bullet"></span>Training of an Internal S3P® Process owner</li>
  </ul>
</main>
</body>
</html>
```